All-natural soap packaging design for new company

The box type has been selected, we just need artwork for each of our 10 products. I'd like the same look to each, the idea is just to switch out the name and ingredient label on each. The dimensions are 3.5"x3.75"x1.25". The colors in the uploaded pictures with product titles are not mandatory. I'd like to keep the font on the packaging (Rubik) as it is the same as the website.

Target Market(s)

Health & Beauty, people looking for natural or organic products

Industry/Entity Type

It Company

Colors

Designer to choose colors to be used in the design.

Requirements
Must have
• Design must be clean and relatively simple. Slightly different look for each of the 10 products. Audience is people looking for all-natural products.

```html
<!DOCTYPE html>
<html lang="en">
<head>
<meta charset="utf-8">
<title>Recipe No. 4 – Soap Box Front Panel</title>
<link href="https://fonts.googleapis.com/css2?family=Oswald:wght@300;400&family=Rubik:wght@300;400;500&display=swap" rel="stylesheet">
<style>
  :root {
    --stage: #d4e1e8;
    --panel: #f7f7f7;
    --leaf: #8dc63f;
    --leaf-light: #a9d35a;
    --leaf-deep: #5f7d34;
    --white: #ffffff;
  }
  html, body {
    margin: 0;
    padding: 0;
    width: 1200px;
    height: 1200px;
    overflow: hidden;
    background: var(--stage);
  }
  .box-front {
    position: absolute;
    left: 120px;
    top: 190px;
    width: 960px;
    height: 820px;
    background: linear-gradient(135deg, var(--white) 0%, var(--panel) 100%);
    overflow: hidden;
    box-shadow: 0 20px 50px rgba(60, 90, 110, 0.18);
  }
  .brand {
    position: absolute;
    right: 90px;
    top: 80px;
    width: 170px;
    display: flex;
    flex-direction: column;
    align-items: center;
    gap: 18px;
  }
  .brand-square {
    width: 120px;
    height: 120px;
    border: 5px solid var(--leaf);
    box-sizing: border-box;
  }
  .brand-name {
    font-family: "Rubik", sans-serif;
    font-weight: 500;
    font-size: 21px;
    letter-spacing: 0.5px;
    color: var(--leaf);
    white-space: nowrap;
  }
  .ingredient-band {
    position: absolute;
    left: 0;
    top: 590px;
    width: 100%;
    height: 150px;
    background: linear-gradient(90deg, var(--leaf) 0%, var(--leaf-light) 100%);
  }
  .recipe-number {
    position: absolute;
    right: 100px;
    top: 470px;
    margin: 0;
    font-family: "Oswald", sans-serif;
    font-weight: 300;
    font-size: 84px;
    line-height: 1;
    color: var(--leaf);
    text-transform: uppercase;
  }
  .ingredients {
    position: absolute;
    right: 100px;
    top: 606px;
    margin: 0;
    font-family: "Rubik", sans-serif;
    font-weight: 300;
    font-size: 52px;
    line-height: 60px;
    color: var(--white);
    text-align: right;
    text-transform: uppercase;
  }
  .botanical-art {
    position: absolute;
    left: 0;
    top: 250px;
    width: 430px;
    height: 570px;
    border-radius: 0 200px 0 0;
    background: radial-gradient(ellipse at 45% 45%, #7d9a4f 0%, #6a8a3e 45%, rgba(141, 198, 63, 0.55) 100%);
  }
</style>
</head>
<body>
  <main class="box-front">
    <div class="brand">
      <div class="brand-square"></div>
      <span class="brand-name">ALDER SOAP CO.</span>
    </div>

    <div class="ingredient-band"></div>

    <div class="botanical-art" role="img" aria-label="Illustration of jojoba seed pods with leaves and fresh lemongrass stalks"></div>

    <h1 class="recipe-number">Recipe No. 4</h1>
    <p class="ingredients">Jojoba<br>+ Lemongrss</p>
  </main>
</body>
</html>
```